Medical Billing Company needs Trifold Brochure Design

We do medical billing and consulting for all types of medical services including hospitals, clinics, physical therapy, mental health, and all other physician specialties. We want to attract new clients from all areas. This is what we have listed on our LinkedIn page: Korvath Billing and Consulting offers 128 years of combined medical billing, coding, credentialing, auditing, and practice management experience. Integrity, reliability, dedication, and open communication are the cornerstones of our foundation. We strive to create meaningful relationships with our clients so they may focus on what they do best, and allow us to handle the rest.

We understand the changes occurring in our healthcare system. Reimbursement is decreasing, expenses are increasing, and the dedication and tenacity to collect every dollar due from the carriers is vital to the financial health of the hospital or practitioner.

Target Market(s)

Physicians, hospitals and any other providers in the medical field such as durable medical equipment suppliers and mid-level providers

Font styles to use
Sans Serif

Colors

Designer to choose colors to be used in the design.

Requirements
Must have
• Specifics list of services we offer. List attached.

```html
<!DOCTYPE html>
<html lang="en">
<head>
<meta charset="utf-8">
<title>Korvath Billing and Consulting – Trifold Brochure</title>
<link href="https://fonts.googleapis.com/css2?family=Open+Sans:wght@400;600;700&family=Roboto+Condensed:wght@400;700&display=swap" rel="stylesheet">
<style>
  :root{
    --green:#4cb046;
    --green-dark:#2f8b3b;
    --green-light:#7cc96f;
    --ink:#2d3a33;
    --muted:#5b6760;
    --paper:#ffffff;
    --stage:#ffffff;
    --photo-doctor-a:#c9d2d6;
    --photo-doctor-b:#e9eef0;
    --photo-desk-a:#b7c3b0;
    --photo-desk-b:#e3e8df;
  }
  *{box-sizing:border-box;margin:0;padding:0}
  html,body{width:876px;height:1200px;overflow:hidden;background:var(--stage)}
  body{font-family:"Open Sans",Arial,sans-serif;color:var(--ink);position:relative}
  .spread{position:absolute;left:18px;width:840px;height:574px;display:flex;box-shadow:0 0 0 1px #e3e6e4}
  .spread--outside{top:14px}
  .spread--inside{top:612px}
  .panel{position:relative;width:280px;height:100%;overflow:hidden;background:var(--paper)}

  /* outside left */
  .services-panel{background:linear-gradient(180deg,var(--green-light),var(--green));color:#fff;padding:26px 22px}
  .services-panel h2{font-family:"Roboto Condensed",Arial,sans-serif;font-size:22px;font-weight:700;letter-spacing:.5px;margin-bottom:12px}
  .services-list{list-style:none}
  .services-list li{font-size:10.5px;font-weight:700;text-transform:uppercase;line-height:1.25;padding-left:16px;position:relative;margin-bottom:6px}
  .services-list li::before{content:"";position:absolute;left:0;top:3px;width:7px;height:7px;background:#fff}

  /* outside middle */
  .mailer-panel .mailer-top{height:300px;background:var(--green);position:relative}
  .mailer-panel .wave{position:absolute;left:0;bottom:-1px;width:280px;height:60px}
  .address{text-align:center;color:var(--green-dark);font-weight:700;font-size:13px;line-height:1.45;margin-top:24px;text-transform:uppercase}
  .contact{text-align:center;color:var(--green-dark);font-weight:700;font-size:13px;line-height:1.45;margin-top:14px}
  .website{position:absolute;left:0;right:0;bottom:18px;text-align:center;font-size:10px;font-weight:600;color:var(--green-dark)}

  /* outside right (cover) */
  .brand{display:flex;align-items:center;gap:8px;padding:22px 20px 0 88px;height:86px}
  .brand-mark{width:14px;height:14px;background:var(--green);flex:none}
  .brand-name{font-weight:700;color:var(--green-dark);font-size:15px;line-height:1.1}
  .cover-photo{height:300px;background:linear-gradient(160deg,var(--photo-doctor-b),var(--photo-doctor-a))}
  .tagline{background:var(--green);color:#fff;text-align:right;padding:14px 20px 16px;font-family:"Roboto Condensed",Arial,sans-serif;text-transform:uppercase}
  .tagline .small{font-size:17px;display:block}
  .tagline .big{font-size:24px;font-weight:700;display:block;line-height:1.1}
  .cover-foot{height:100%;background:#eef3ee}

  /* inside */
  .header-photo{height:150px;background:linear-gradient(135deg,var(--photo-desk-b),var(--photo-desk-a))}
  .inside-body{padding:14px 20px}
  .inside-body h3{font-family:"Roboto Condensed",Arial,sans-serif;font-size:24px;color:var(--green);font-weight:700;text-transform:uppercase;margin-bottom:8px}
  .inside-body h3.sub{font-size:20px;line-height:1.1;margin-top:16px}
  .inside-body p{font-size:10px;line-height:1.5;color:var(--muted)}
  .inside-body ul{list-style:none;margin-top:2px}
  .inside-body li{font-size:10px;line-height:1.45;color:var(--muted);padding-left:12px;position:relative}
  .inside-body li::before{content:"";position:absolute;left:0;top:5px;width:5px;height:5px;background:var(--green)}

  .glance-panel{background:linear-gradient(180deg,var(--green),var(--green-dark));color:#fff}
  .glance-panel .header-photo{opacity:.55}
  .badge{position:absolute;left:-18px;top:70px;width:96px;height:96px;border-radius:50%;background:var(--green-dark);border:3px solid #fff;color:#fff;font-size:9px;font-weight:700;text-align:center;text-transform:uppercase;display:flex;align-items:center;justify-content:center;padding:10px;line-height:1.25;z-index:2}
  .glance-body{padding:18px 22px}
  .glance-body h3{font-family:"Roboto Condensed",Arial,sans-serif;font-size:28px;font-weight:400;text-transform:uppercase;line-height:1.05;margin-bottom:12px}
  .glance-body h4{font-size:13px;font-weight:700;margin-bottom:8px}
  .glance-body p{font-size:10px;line-height:1.5;margin-bottom:10px}
  .cta{margin-top:20px;font-family:"Roboto Condensed",Arial,sans-serif}
  .cta .phone{font-size:24px;font-weight:700;display:block}
  .cta .offer{font-size:18px;display:block}
  .middle-panel{border-left:1px solid #e3e6e4;border-right:1px solid #e3e6e4}
</style>
</head>
<body>

<section class="spread spread--outside">
  <div class="panel services-panel">
    <h2>SERVICES INCLUDE:</h2>
    <ul class="services-list">
      <li>Electronic &amp; paper claims</li>
      <li>Insurance follow ups</li>
      <li>Monthly patient billing</li>
      <li>Payment posting</li>
      <li>Comprehensive monthly reporting</li>
      <li>Denial management</li>
      <li>Insurance appeals</li>
      <li>Past due claims</li>
      <li>Insurance verification</li>
      <li>Authorization tracking</li>
      <li>Practice consulting</li>
      <li>Remote access consulting</li>
      <li>Tracking and verifying allowables</li>
      <li>Credentialing</li>
      <li>Claim correction and resubmission</li>
      <li>Emergency “fill-in” or transition billing</li>
      <li>Let us work when you can’t</li>
    </ul>
  </div>

  <div class="panel mailer-panel">
    <div class="mailer-top">
      <svg class="wave" viewBox="0 0 280 60" preserveAspectRatio="none">
        <path d="M0 40 C80 10 180 70 280 20 L280 60 L0 60 Z" fill="#ffffff"/>
      </svg>
    </div>
    <p class="address">418 Larkspur Row<br>Mesa Alta, NM 88011</p>
    <p class="contact">TEL: 505.214.7730<br>FAX: 866.302.5591</p>
    <p class="website">www.korvathbilling.com</p>
  </div>

  <div class="panel cover-panel">
    <div class="brand">
      <span class="brand-mark"></span>
      <span class="brand-name">Korvath Billing<br>and Consulting</span>
    </div>
    <div class="cover-photo" role="img" aria-label="Photo of a physician in a white coat with a stethoscope"></div>
    <div class="tagline">
      <span class="small">The best medicine</span>
      <span class="big">for a broken<br>billing cycle</span>
    </div>
    <div class="cover-foot"></div>
  </div>
</section>

<section class="spread spread--inside">
  <div class="panel">
    <div class="header-photo" role="img" aria-label="Photo of financial charts and a calculator on a desk"></div>
    <div class="inside-body">
      <h3>Welcome</h3>
      <p>Korvath Billing and Consulting is here to help you and your business. We will work closely with your team to create a billing process that lets you focus on patient care while we handle the rest.</p>
      <h3 class="sub">Services</h3>
      <ul>
        <li>All of CMS1500 / UB04 Billing</li>
        <li>Bill Insurance Providers</li>
        <li>Third Party Insurance</li>
        <li>Monitoring Claims</li>
        <li>Reviewing and Billing Accounts</li>
        <li>Receivable Procedures</li>
        <li>Medicare Billing</li>
        <li>Cash Flow Reporting</li>
        <li>Work in local EMR software</li>
        <li>Work in your system or ours</li>
      </ul>
    </div>
  </div>

  <div class="panel middle-panel">
    <div class="header-photo" role="img" aria-label="Photo of hands reviewing printed billing reports"></div>
    <div class="inside-body">
      <h3>Achievement</h3>
      <p>We know your company is mind and caring, and your goals are able to make your company successful. Whether you are billing or preparing one for a Medicare audit we will help you to get the most out of every claim you submit to the carrier.</p>
      <h3 class="sub">Our Key Solution<br>Benefits:</h3>
      <ul>
        <li>Review AR to turn into cash</li>
        <li>Experienced billers working for you</li>
        <li>Eliminate employee costs</li>
        <li>No contract commitment or insurance</li>
        <li>Maximizing your returns</li>
      </ul>
    </div>
  </div>

  <div class="panel glance-panel">
    <div class="badge">Quick cost effective efficient billing solutions</div>
    <div class="header-photo" role="img" aria-label="Photo of a medical team at work"></div>
    <div class="glance-body">
      <h3>Our Company<br>at a Glance</h3>
      <h4>Korvath Billing and Consulting</h4>
      <p>Here at Korvath Billing and Consulting, we are dedicated to our part of your efficient billing cycle.</p>
      <p>We have over 128 years of billing experience. Our experienced team specializes in coding and billing for all medical specialties and practices of every size.</p>
      <div class="cta">
        <span class="phone">Call 505-214-7730</span>
        <span class="offer">For A Free Consultation</span>
      </div>
    </div>
  </div>
</section>

</body>
</html>
```